Up and Coming Granola Brand Needs Labels and Logo Design

We need a label design for a new Granola Company called Pem's Granola. We create delicious hand-crafted granolas that are not only tasty, but good for you!

We would also like a 'modern' logo, similar to the attached one.
The logo name is "Pem's". The concept would be to have the word "Pem's" in the banner, and "Granola" below in font. Eventually the product line will expand to include other items, and we would like a logo that allows us to match the product to the logo name.

The logo should integrate well with the packaging label.

We plan on using light brown resealable packaging for our granola, and would prefer earthy colours, or colours that would complement the packaging for the labels. We intend to print the designs on labels, and paste them on the front and back of the package. (Package dimensions and image of package are included in attachments)

We plan on having a few flavours of Granola, and that would have some small changes on the label design.

Some of our ingredients in our granola would include Oats, Dried fruit, nuts and various grains.

It would be good if the labels could feature oats (perhaps an ear of oats, or something to similar effect)
Updates

have added dimensions to the packaging to give a sense of size for reference. image of the packaging we will be using also added! Added Wednesday, May 11, 2016

Reason: Loving the submissions so far! Can't wait to see what else you can come up with! Have extended the deadline to give some breathing room and time for tweaking!

Target Market(s)

20s-40s

Industry/Entity Type

Food Store

Logo Text

Pem's

Font styles to use
Serif
Decorative

Requirements
Must have
• -Colours that complement the packaging colour (light brown)
• -Can be printed on white labels that will be stuck on the packaging (both for the front of packaging; that has a window, and the back of the packaging; no window)
• -simple and stylish design that entices buyers to purchase the product
• -A flexible logo that can transition seamlessly between different product lines
• - Sections for "our story", "nutritional information", "ingredients, etc on the back label.
Nice to have
• -as attached in image samples for the brief.
• - other trendy designs that are currently popular
• - different colour schemes for different flavours. Currently there are 3 flavours; 1) Mocha Almond, 2) Matcha with White Chocolate and Cashews, and 3) Classic Fruit and Nut.
Should not have
• -colours that stand out too much, or do not fit the design brief
• -overly complicated designs that take away from the main theme of awesome granola

```html
<!DOCTYPE html>
<html lang="en">
<head>
<meta charset="utf-8">
<title>Pem's Granola – Dried Fruit &amp; Oats Labels</title>
<link rel="stylesheet" href="https://fonts.googleapis.com/css2?family=Oranienbaum&family=Oswald:wght@400;500&family=Roboto:wght@400;700&display=swap">
<style>
  :root {
    --backdrop: #857a70;
    --slate: #3d4f58;
    --slate-light: #5b6e77;
    --band-dark: #5e4c45;
    --band-light: #8a7168;
    --cream: #f1ece2;
    --ink: #111;
    --paper: #fff;
  }
  * { box-sizing: border-box; margin: 0; padding: 0; }
  html, body { width: 1200px; height: 900px; overflow: hidden; }
  body { background: var(--backdrop); position: relative; font-family: "Oswald", sans-serif; }

  .label {
    position: absolute;
    top: 275px;
    width: 555px;
    height: 350px;
    border-radius: 16px;
    overflow: hidden;
    background: radial-gradient(ellipse at 50% 35%, var(--slate-light), var(--slate) 75%);
    color: var(--cream);
  }
  .label--front { left: 30px; }
  .label--back { left: 615px; }

  .label__band {
    position: absolute; left: 0; right: 0; bottom: 0; height: 44px;
    background: linear-gradient(180deg, var(--band-dark), var(--band-light));
    display: flex; align-items: center;
    font-family: "Oranienbaum", serif; font-size: 24px; word-spacing: 10px;
  }
  .label--front .label__band { justify-content: center; }
  .label--back .label__band { padding-left: 24px; }

  .brand-name { font-family: "Oranienbaum", serif; color: var(--cream); font-weight: 400; white-space: nowrap; }

  /* front */
  .front__eyebrow {
    position: absolute; top: 22px; width: 100%; text-align: center;
    font-size: 24px; letter-spacing: 8px;
  }
  .front__brand { position: absolute; top: 62px; width: 100%; text-align: center; font-size: 86px; line-height: 1; }
  .front__with {
    position: absolute; top: 168px; width: 100%; text-align: center;
    font-size: 18px; letter-spacing: 4px;
  }
  .front__flavour {
    position: absolute; top: 196px; width: 100%; text-align: center;
    font-family: "Oranienbaum", serif; font-weight: 400; font-size: 66px; line-height: 1;
  }

  /* back */
  .back__header {
    position: absolute; top: 22px; left: 24px; right: 22px; height: 56px;
    display: flex; align-items: center; justify-content: space-between; gap: 16px;
  }
  .back__brand { font-size: 24px; line-height: 1; }
  .back__flavour {
    font-family: "Oranienbaum", serif; font-weight: 400; font-size: 44px; line-height: 1; white-space: nowrap;
  }
  .back__copy {
    position: absolute; top: 96px; left: 24px; width: 322px;
    display: flex; flex-direction: column; gap: 12px;
  }
  .back__story {
    font-size: 10.5px; line-height: 1.45; text-transform: uppercase; text-align: justify; letter-spacing: .2px;
  }
  .back__ingredients { font-size: 10.5px; line-height: 1.45; }
  .back__ingredients strong { font-weight: 500; }

  .nutrition {
    position: absolute; top: 92px; right: 22px; width: 168px; height: 214px;
    background: var(--paper); color: var(--ink); border: 1px solid var(--ink);
    padding: 4px 6px; font-family: "Roboto", sans-serif; font-size: 7.5px; line-height: 1.35;
  }
  .nutrition__title { font-weight: 700; font-size: 17px; line-height: 1.1; border-bottom: 1px solid var(--ink); }
  .nutrition__rule-thick { border-top: 5px solid var(--ink); margin: 2px 0; }
  .nutrition__rule { border-top: 1px solid var(--ink); }
  .nutrition__row { display: flex; justify-content: space-between; border-top: 1px solid #999; }
  .nutrition__row--indent { padding-left: 8px; }
  .nutrition__row b { font-weight: 700; }
  .nutrition__dv { text-align: right; font-weight: 700; font-size: 6.5px; }
  .nutrition__note { font-size: 6px; color: #444; margin-top: 3px; }
</style>
</head>
<body>

<section class="label label--front" aria-label="Front label">
  <p class="front__eyebrow">ORIGINAL</p>
  <h1 class="front__brand brand-name">Pem's Granola</h1>
  <p class="front__with">WITH</p>
  <h2 class="front__flavour">Dried Fruit &amp; Oats</h2>
  <div class="label__band">100g 3,5 oz</div>
</section>

<section class="label label--back" aria-label="Back label">
  <div class="back__header">
    <p class="back__brand brand-name">Pem's Granola</p>
    <h2 class="back__flavour">Dried Fruit &amp; Oats</h2>
  </div>

  <div class="back__copy">
    <p class="back__story">Granola is an extremely popular breakfast and snack food with a wealth of health benefits, including its ability to lower cholesterol, regulate digestion, aid in weight loss attempts, improve your heart health, increase energy, prevent anemia and promote proper organ function.</p>
    <p class="back__ingredients"><strong>Ingredients:</strong> Oat bran, almonds, whey protein isolate, flaxseed, amber honey, rolled oats, raisins, molasses, chicory root, expeller pressed non-GMO canola oil, baking powder, cinnamon, vanilla, maple, salt, tocopherols, stevia.</p>
  </div>

  <div class="nutrition" aria-label="Nutrition facts">
    <div class="nutrition__title">Nutrition Facts</div>
    <div>Serving Size 1 cup (35g)</div>
    <div>Servings Per Container 25</div>
    <div class="nutrition__rule-thick"></div>
    <div>Amount Per Serving</div>
    <div class="nutrition__row"><span><b>Calories</b> 140</span><span>Calories from Fat 32</span></div>
    <div class="nutrition__rule"></div>
    <div class="nutrition__dv">% Daily Value*</div>
    <div class="nutrition__row"><span><b>Total Fat</b> 3.5g</span><b>5%</b></div>
    <div class="nutrition__row nutrition__row--indent"><span>Saturated Fat 2.5g</span><b>13%</b></div>
    <div class="nutrition__row nutrition__row--indent"><span>Trans Fat 0g</span><span></span></div>
    <div class="nutrition__row"><span><b>Sodium</b> 110mg</span><b>5%</b></div>
    <div class="nutrition__row"><span><b>Total Carbohydrate</b> 24g</span><b>8%</b></div>
    <div class="nutrition__row nutrition__row--indent"><span>Dietary Fiber 1g</span><b>4%</b></div>
    <div class="nutrition__row nutrition__row--indent"><span>Sugars 15g</span><span></span></div>
    <div class="nutrition__row"><span><b>Protein</b> 3g</span><b>4%</b></div>
    <div class="nutrition__rule-thick"></div>
    <div class="nutrition__note">*Percent Daily Values are based on a 2,000 calorie diet.</div>
  </div>

  <div class="label__band">100g 3,5 oz</div>
</section>

</body>
</html>
```